Business Cards for Tech Company - uBrightowl

We would like new modern business cards designed for our company. Attached are some examples of other business cards we like. <br/><br/>Info we need is: <br/>First Name, Last Name<br/>Address<br/>Store Phone<br/>Cell Phone<br/>Email Address<br/>Text Logo <br/>And Other Logo<br/>

Industry/Entity Type

Technology Equipment

Contact Information for Business Card

Please use these details as example:

Dale Morrow
Technology Specialist
Direct 555.617.2094
Phone 555-730-8186

dale.morrow@ubrightowl.example

2971 Willet Lane
Larkfield, NV 00427

Font styles to use
Sans Serif
Other font styles liked:
• Anything easy to read and modern

Colors

Designer to choose colors to be used in the design.

Requirements
Must have
• Both Logos
• Signature as name
• Use the text logo and use the shark logo but do not use the full shark logo. Have it where it is zoomed in and is expanding out of the card.
Nice to have
• Keep it clean and modern
• We like blue, white, and black/grays.
Should not have
• Random icons for phone and address.

```html
<!DOCTYPE html>
<html lang="en">
<head>
<meta charset="utf-8">
<title>uBrightowl Business Cards</title>
<link rel="stylesheet" href="https://fonts.googleapis.com/css2?family=Lato:wght@300;400;700;900&display=swap">
<style>
  :root {
    --brand-blue: #1479f0;
    --ink-dark: #2b2a2d;
    --logo-grey: #7d7f84;
    --text-grey: #8e9095;
    --paper: #ffffff;
    --ghost-tint: #eaf1fb;
    --stage: #e9eaec;
  }
  * { box-sizing: border-box; margin: 0; padding: 0; }
  html, body {
    width: 1200px;
    height: 1200px;
    overflow: hidden;
    background: var(--stage);
    font-family: "Lato", Arial, sans-serif;
  }
  .sheet {
    width: 1200px;
    height: 1200px;
    display: flex;
    flex-direction: column;
    align-items: center;
    justify-content: center;
    gap: 70px;
  }
  .card {
    position: relative;
    width: 840px;
    height: 480px;
    background: var(--paper);
    border-radius: 26px;
    overflow: hidden;
    box-shadow: 0 14px 34px rgba(0, 0, 0, 0.14);
  }

  /* Front */
  .card-front .mark-ghost {
    position: absolute;
    left: 70px;
    top: -40px;
    width: 260px;
    height: 420px;
    border-radius: 50% 50% 46% 46%;
    background: var(--ghost-tint);
  }
  .wordmark {
    display: flex;
    align-items: center;
    gap: 12px;
    font-family: "Lato", Arial, sans-serif;
    font-weight: 900;
    color: var(--logo-grey);
    letter-spacing: -0.5px;
    white-space: nowrap;
  }
  .wordmark .wordmark-dot {
    border-radius: 50%;
    background: var(--brand-blue);
    flex: none;
  }
  .card-front .wordmark {
    position: absolute;
    left: 350px;
    top: 175px;
    font-size: 58px;
  }
  .card-front .wordmark .wordmark-dot { width: 26px; height: 26px; }
  .card-front .front-email {
    position: absolute;
    right: 112px;
    top: 352px;
    font-size: 19px;
    font-weight: 400;
    color: var(--text-grey);
    white-space: nowrap;
  }
  .card-front .band {
    position: absolute;
    left: 0;
    bottom: 0;
    width: 100%;
    height: 62px;
    display: flex;
  }
  .band .band-blue { width: 60%; background: var(--brand-blue); }
  .band .band-dark { width: 40%; background: var(--ink-dark); }

  /* Back */
  .card-back .contact-panel {
    position: absolute;
    left: 0;
    top: 0;
    width: 400px;
    height: 100%;
    background: var(--brand-blue);
    color: var(--paper);
    padding: 92px 0 0 70px;
  }
  .card-back .accent-bar {
    position: absolute;
    left: 400px;
    top: 70px;
    width: 14px;
    height: 240px;
    background: var(--ink-dark);
  }
  .holder-name {
    font-size: 34px;
    font-weight: 700;
    text-transform: uppercase;
    letter-spacing: 0.5px;
    line-height: 1.05;
    white-space: nowrap;
  }
  .holder-title {
    font-size: 25px;
    font-weight: 300;
    margin-top: 2px;
  }
  .title-rule {
    width: 130px;
    height: 2px;
    background: var(--paper);
    margin: 16px 0 22px;
  }
  .contact-list { list-style: none; }
  .contact-list li {
    display: flex;
    align-items: flex-start;
    gap: 14px;
    font-size: 17px;
    line-height: 1.25;
    margin-bottom: 16px;
    white-space: nowrap;
  }
  .contact-list svg {
    width: 20px;
    height: 20px;
    flex: none;
    margin-top: 2px;
    fill: var(--paper);
  }
  .card-back .wordmark {
    position: absolute;
    left: 492px;
    top: 200px;
    font-size: 52px;
  }
  .card-back .wordmark .wordmark-dot { width: 22px; height: 22px; }
</style>
</head>
<body>
<main class="sheet">

  <section class="card card-front" aria-label="Business card front">
    <div class="mark-ghost" role="img" aria-label="Faint enlarged brand symbol bleeding off the card edge"></div>
    <div class="wordmark">
      <span class="wordmark-dot"></span>
      <span class="wordmark-name">uBrightowl</span>
    </div>
    <p class="front-email">dale.morrow@ubrightowl.example</p>
    <div class="band">
      <div class="band-blue"></div>
      <div class="band-dark"></div>
    </div>
  </section>

  <section class="card card-back" aria-label="Business card back">
    <div class="contact-panel">
      <h1 class="holder-name">Dale Morrow</h1>
      <p class="holder-title">Technology Specialist</p>
      <div class="title-rule"></div>
      <ul class="contact-list">
        <li>
          <svg viewBox="0 0 20 20" aria-hidden="true"><path d="M1 4h18v12H1z M2 5l8 6 8-6" fill="none" stroke="#fff" stroke-width="1.6"/><path d="M1 4h18L10 11z"/></svg>
          <span>dale.morrow@ubrightowl.example</span>
        </li>
        <li>
          <svg viewBox="0 0 20 20" aria-hidden="true"><path d="M5 2l3 4-2 2c1 2.5 3.5 5 6 6l2-2 4 3-2 3C9 18 2 11 2 4z"/></svg>
          <span>Phone 555-730-8186<br>Direct 555.617.2094</span>
        </li>
        <li>
          <svg viewBox="0 0 20 20" aria-hidden="true"><path d="M10 2L1 10h3v8h5v-5h2v5h5v-8h3z"/></svg>
          <span>2971 Willet Lane<br>Larkfield, NV 00427</span>
        </li>
      </ul>
    </div>
    <div class="accent-bar"></div>
    <div class="wordmark">
      <span class="wordmark-dot"></span>
      <span class="wordmark-name">uBrightowl</span>
    </div>
  </section>

</main>
</body>
</html>
```